Financial Dashboard UI design

We are building a financial dashboard for business management teams, and would like a futuristic and sophisticated design (light and dark themes).

There are a total of 3 screens (attached images: nemo1, nemo2, nemo3).
nemo1 image is comprised of 6 scorecards (attached image: scorecard)
This will also need a design.

So, I'm expecting 4 UI designs in total.

I've added some example UI for inspiration. (sample1 , sample2, sample3, sample4).

Thanks

```html
<!DOCTYPE html>
<html lang="en">
<head>
<meta charset="utf-8">
<title>Financial Dashboard</title>
<link href="https://fonts.googleapis.com/css2?family=Roboto:wght@400;500;700&display=swap" rel="stylesheet">
<style>
:root{
  --stage:#bdbdbd;
  --navy-top:#222a7c;
  --navy-bottom:#3a44a0;
  --brand:#2b35a0;
  --cyan:#22c1fb;
  --green:#a6e4a6;
  --alert:#ff0000;
  --ink:#222;
  --text:#333;
  --muted:#999;
  --line:#d9d9d9;
  --white:#fff;
}
*{box-sizing:border-box;margin:0;padding:0}
html,body{width:892px;height:1200px;overflow:hidden}
body{background:var(--stage);font-family:'Roboto',sans-serif;position:relative}
.screen{position:absolute;left:66px;width:760px;height:498px;background:var(--white);overflow:hidden}
.screen--sales{top:69px}
.screen--budget{top:632px}
.sidebar{position:absolute;left:0;top:0;width:113px;height:100%;background:linear-gradient(180deg,var(--navy-top),var(--navy-bottom))}
.nav{list-style:none;padding-top:16px}
.nav__item{position:relative;height:23.8px;display:flex;align-items:center;padding-left:22px;color:var(--white);font-size:8px;width:109px}
.nav__item--active{background:var(--cyan);border-radius:0 12px 12px 0}
.nav__icon{width:8px;height:8px;margin-right:12px;fill:var(--white)}
.search{position:absolute;left:141px;top:15px;width:228px;height:30px;border:1px solid #ddd;border-radius:15px;display:flex;align-items:center;padding:0 14px;font-size:7.5px;color:#555}
.search__icon{position:absolute;right:15px;top:10px;width:9px;height:9px}
.topbar__search{position:absolute;left:549px;top:21px;width:9px;height:9px}
.lang{position:absolute;left:575px;top:15px;display:flex;align-items:center;font-size:8px;color:var(--ink)}
.lang__flag{width:22px;height:22px;border-radius:50%;margin-right:5px;background:linear-gradient(180deg,#2b3a8c 0 45%,#d33 45% 55%,#fff 55% 65%,#d33 65% 78%,#fff 78% 88%,#d33 88%)}
.lang__caret{margin-left:2px;width:5px;height:5px}
.bell{position:absolute;left:649px;top:21px;width:9px;height:10px}
.user{position:absolute;left:674px;top:15px;display:flex;align-items:center;font-size:8px;color:var(--ink)}
.user__avatar{width:22px;height:22px;border-radius:50%;background:linear-gradient(160deg,#c9a88a,#6b5547);margin-right:5px}
.page-title{position:absolute;left:150px;top:71px;font-size:14px;font-weight:700;color:var(--brand)}
.page-meta{position:absolute;left:261px;top:77px;font-size:8px;font-weight:500;color:var(--ink)}
.card{position:absolute;left:141px;top:99px;width:590px;height:420px;background:var(--white);border-radius:14px;box-shadow:0 1px 6px rgba(0,0,0,.18);overflow:hidden}
.card__stripe{position:absolute;top:36px;bottom:0}
.card__stripe--country{left:72.4px;width:59.9px;background:var(--cyan)}
.card__stripe--total{left:361.1px;width:60.5px;background:var(--green)}
.sales{position:relative;border-collapse:collapse;table-layout:fixed;width:590px}
.sales th{height:36px;background:var(--brand);color:var(--white);font-size:7px;font-weight:700;position:relative}
.sales th+th::after{content:"";position:absolute;left:0;top:12px;height:11px;border-left:1px solid rgba(255,255,255,.7)}
.sales td{height:23.8px;font-size:6.4px;color:var(--text);text-align:center;white-space:nowrap}
.sales tbody tr:first-child td{padding-top:6px;height:29px}
.sales .c-country{color:var(--white);text-align:left;padding-left:11px}
.sales .c-area{text-align:left;padding-left:12px}
.sales .c-total{text-align:left;padding-left:6px}
.sales .c-right{text-align:left;padding-left:3px}
.sales .flag{background:var(--alert);color:var(--white)}
.budget-title{position:absolute;left:151px;top:70px;font-size:14px;font-weight:700;color:var(--ink)}
.charts{position:absolute;left:0;top:0;width:760px;height:498px}
.legend{position:absolute;left:439px;top:67px;width:119px;height:214px;border-radius:13px;background:var(--white);box-shadow:0 1px 6px rgba(0,0,0,.15);list-style:none;padding:7px 0 0 11px}
.legend li{display:flex;align-items:center;height:11.9px;font-size:5.8px;font-weight:700;color:var(--ink)}
.legend i{width:4.5px;height:4.5px;border-radius:50%;margin-right:6px;display:block}
</style>
</head>
<body>

<svg width="0" height="0" style="position:absolute">
  <defs>
    <symbol id="i-home" viewBox="0 0 10 10"><path d="M5 1 0 5.5h1.5V9h2.5V6.5h2V9h2.5V5.5H10z"/></symbol>
    <symbol id="i-chart" viewBox="0 0 10 10"><path d="M0 0h1v9h9v1H0zM2 5h1.5v3H2zM4.5 3H6v5H4.5zM7 4h1.5v4H7z"/></symbol>
    <symbol id="i-mail" viewBox="0 0 10 10"><path d="M0 2h10v6H0zM0 2l5 3.5L10 2" stroke="#2b35a0" stroke-width=".6"/></symbol>
    <symbol id="i-cal" viewBox="0 0 10 10"><path d="M1 2h8v7H1zM2.5 0h1v2h-1zM6.5 0h1v2h-1z"/></symbol>
    <symbol id="i-list" viewBox="0 0 10 10"><path d="M0 1h10v2H0zM0 4h10v2H0zM0 7h10v2H0z"/></symbol>
    <symbol id="i-bino" viewBox="0 0 10 10"><path d="M1 2h3v8H0V5zM6 2h3l1 3v5H6zM4 4h2v3H4z"/></symbol>
    <symbol id="i-user" viewBox="0 0 10 10"><circle cx="5" cy="3" r="2.5"/><path d="M1 10c0-3 1.5-4 4-4s4 1 4 4z"/></symbol>
    <symbol id="i-help" viewBox="0 0 10 10"><circle cx="5" cy="5" r="5"/></symbol>
    <symbol id="i-warn" viewBox="0 0 10 10"><path d="M5 0 10 10H0z"/></symbol>
    <symbol id="i-search" viewBox="0 0 10 10"><circle cx="4" cy="4" r="3" fill="none" stroke="currentColor" stroke-width="1.5"/><path d="M6 6l3.5 3.5" stroke="currentColor" stroke-width="1.6"/></symbol>
    <symbol id="i-cart" viewBox="0 0 10 10"><path d="M0 1h2l1 5h6l1-4H2.5" fill="none" stroke="#fff" stroke-width="1.2"/><circle cx="3.5" cy="8.5" r="1"/><circle cx="8" cy="8.5" r="1"/></symbol>
    <symbol id="i-gear" viewBox="0 0 10 10"><circle cx="5" cy="5" r="3.2" fill="none" stroke="#fff" stroke-width="2.2" stroke-dasharray="1.4 .9"/><circle cx="5" cy="5" r="2.2"/></symbol>
    <symbol id="i-bell" viewBox="0 0 10 10"><path d="M5 0C3 0 2 2 2 4v3L1 8h8L8 7V4C8 2 7 0 5 0zM4 9h2a1 1 0 0 1-2 0z"/></symbol>
    <symbol id="i-caret" viewBox="0 0 10 10"><path d="M1 3l4 4 4-4" fill="none" stroke="currentColor" stroke-width="1.4"/></symbol>
  </defs>
</svg>

<!-- Sales table screen -->
<section class="screen screen--sales">
  <aside class="sidebar">
    <ul class="nav">
      <li class="nav__item nav__item--active"><svg class="nav__icon"><use href="#i-home"/></svg>Report</li>
      <li class="nav__item"><svg class="nav__icon"><use href="#i-chart"/></svg>Charts</li>
      <li class="nav__item"><svg class="nav__icon"><use href="#i-mail"/></svg>Email</li>
      <li class="nav__item"><svg class="nav__icon"><use href="#i-cal"/></svg>Calendar</li>
      <li class="nav__item"><svg class="nav__icon"><use href="#i-list"/></svg>Nodification</li>
      <li class="nav__item"><svg class="nav__icon"><use href="#i-bino"/></svg>Stand-in</li>
      <li class="nav__item"><svg class="nav__icon"><use href="#i-user"/></svg>Tasks</li>
      <li class="nav__item"><svg class="nav__icon"><use href="#i-help"/></svg>Market</li>
      <li class="nav__item"><svg class="nav__icon"><use href="#i-warn"/></svg>News</li>
      <li class="nav__item"><svg class="nav__icon" style="color:#fff"><use href="#i-search"/></svg>Search</li>
      <li class="nav__item"><svg class="nav__icon"><use href="#i-cart"/></svg>Glossary</li>
      <li class="nav__item"><svg class="nav__icon"><use href="#i-gear"/></svg>Setting</li>
    </ul>
  </aside>
  <div class="search">Enter your keyword<svg class="search__icon" style="color:#333"><use href="#i-search"/></svg></div>
  <svg class="topbar__search" style="color:#222"><use href="#i-search"/></svg>
  <div class="lang"><span class="lang__flag" role="img" aria-label="Language flag"></span>English<svg class="lang__caret" style="color:#222"><use href="#i-caret"/></svg></div>
  <svg class="bell" style="fill:#222"><use href="#i-bell"/></svg>
  <div class="user"><span class="user__avatar" role="img" aria-label="User avatar photo"></span>Sam Reed</div>

  <h1 class="page-title">2021 U.S SALES</h1>
  <p class="page-meta">Page 1/107 (2886 records)</p>

  <div class="card">
    <div class="card__stripe card__stripe--country"></div>
    <div class="card__stripe card__stripe--total"></div>
    <table class="sales">
      <colgroup>
        <col style="width:72.4px"><col style="width:59.9px"><col style="width:83.7px"><col style="width:59.9px"><col style="width:33.5px"><col style="width:51.8px"><col style="width:60.5px"><col style="width:35.1px"><col style="width:73.4px"><col style="width:59.8px">
      </colgroup>
      <thead>
        <tr><th>STYLEINDEX</th><th>COUNTRY</th><th>BUISNESS AREA</th><th>ACTUAL</th><th>PLA</th><th>FORECAST</th><th>TOTAL</th><th>RIGHT</th><th>IT SUB AREA</th><th>SAME</th></tr>
      </thead>
      <tbody>
        <tr><td>Administration</td><td class="c-country">Germany</td><td class="c-area">Distribution</td><td>50598.8</td><td>0</td><td>0</td><td class="c-total">2560965547.63</td><td class="c-right">ny</td><td>Administration</td><td>50708</td></tr>
        <tr><td>Administration</td><td class="c-country">Germany</td><td class="c-area">Distribution</td><td>50598.8</td><td>0</td><td>0</td><td class="c-total">2560965547.63</td><td class="c-right">ny</td><td>Administration</td><td>50708</td></tr>
        <tr><td>Administration</td><td class="c-country">Germany</td><td class="c-area">Distribution</td><td>50598.8</td><td>0</td><td>0</td><td class="c-total">2560965547.63</td><td class="c-right">ny</td><td>Administration</td><td>50708</td></tr>
        <tr><td>Administration</td><td class="c-country">Germany</td><td class="c-area">Distribution</td><td>50598.8</td><td>0</td><td>0</td><td class="c-total">2560965547.63</td><td class="c-right">ny</td><td>Administration</td><td>50708</td></tr>
        <tr><td>Administration</td><td class="c-country">Germany</td><td class="c-area">Distribution</td><td>50598.8</td><td>0</td><td>0</td><td class="c-total">2560965547.63</td><td class="c-right">ny</td><td>Administration</td><td>50708</td></tr>
        <tr><td>Administration</td><td class="c-country">Germany</td><td class="c-area">Distribution</td><td>50598.8</td><td>0</td><td>0</td><td class="c-total">2560965547.63</td><td class="c-right">ny</td><td>Administration</td><td>50708</td></tr>
        <tr><td>Administration</td><td class="c-country">Germany</td><td class="c-area">Distribution</td><td>50598.8</td><td>0</td><td>0</td><td class="c-total">2560965547.63</td><td class="c-right">ny</td><td>Administration</td><td class="flag">50708</td></tr>
        <tr><td>Administration</td><td class="c-country">Germany</td><td class="c-area">Distribution</td><td>50598.8</td><td>0</td><td>0</td><td class="c-total">2560965547.63</td><td class="c-right">ny</td><td>Administration</td><td class="flag">50708</td></tr>
        <tr><td>Administration</td><td class="c-country">Germany</td><td class="c-area">Distribution</td><td>50598.8</td><td>0</td><td>0</td><td class="c-total">2560965547.63</td><td class="c-right">ny</td><td>Administration</td><td class="flag">50708</td></tr>
        <tr><td>Administration</td><td class="c-country">Germany</td><td class="c-area">Distribution</td><td>50598.8</td><td>0</td><td>0</td><td class="c-total">2560965547.63</td><td class="c-right">ny</td><td>Administration</td><td class="flag">50708</td></tr>
        <tr><td>Administration</td><td class="c-country">Germany</td><td class="c-area">Distribution</td><td>50598.8</td><td>0</td><td>0</td><td class="c-total">2560965547.63</td><td class="c-right">ny</td><td>Administration</td><td>50708</td></tr>
        <tr><td>Administration</td><td class="c-country">Germany</td><td class="c-area">Distribution</td><td>50598.8</td><td>0</td><td>0</td><td class="c-total">2560965547.63</td><td class="c-right">ny</td><td>Administration</td><td>50708</td></tr>
        <tr><td>Administration</td><td class="c-country">Germany</td><td class="c-area">Distribution</td><td>50598.8</td><td>0</td><td>0</td><td class="c-total">2560965547.63</td><td class="c-right">ny</td><td>Administration</td><td>50708</td></tr>
        <tr><td>Administration</td><td class="c-country">Germany</td><td class="c-area">Distribution</td><td>50598.8</td><td>0</td><td>0</td><td class="c-total">2560965547.63</td><td class="c-right">ny</td><td>Administration</td><td>50708</td></tr>
      </tbody>
    </table>
  </div>
</section>

<!-- Budget charts screen -->
<section class="screen screen--budget">
  <aside class="sidebar">
    <ul class="nav">
      <li class="nav__item"><svg class="nav__icon"><use href="#i-home"/></svg>Report</li>
      <li class="nav__item nav__item--active"><svg class="nav__icon"><use href="#i-chart"/></svg>Charts</li>
      <li class="nav__item"><svg class="nav__icon"><use href="#i-mail"/></svg>Email</li>
      <li class="nav__item"><svg class="nav__icon"><use href="#i-cal"/></svg>Calendar</li>
      <li class="nav__item"><svg class="nav__icon"><use href="#i-list"/></svg>Nodification</li>
      <li class="nav__item"><svg class="nav__icon"><use href="#i-bino"/></svg>Stand-in</li>
      <li class="nav__item"><svg class="nav__icon"><use href="#i-user"/></svg>Tasks</li>
      <li class="nav__item"><svg class="nav__icon"><use href="#i-help"/></svg>Market</li>
      <li class="nav__item"><svg class="nav__icon"><use href="#i-warn"/></svg>News</li>
      <li class="nav__item"><svg class="nav__icon" style="color:#fff"><use href="#i-search"/></svg>Search</li>
      <li class="nav__item"><svg class="nav__icon"><use href="#i-cart"/></svg>Glossary</li>
      <li class="nav__item"><svg class="nav__icon"><use href="#i-gear"/></svg>Setting</li>
    </ul>
  </aside>
  <div class="search">Enter your keyword<svg class="search__icon" style="color:#333"><use href="#i-search"/></svg></div>
  <svg class="topbar__search" style="color:#222"><use href="#i-search"/></svg>
  <div class="lang"><span class="lang__flag" role="img" aria-label="Language flag"></span>English<svg class="lang__caret" style="color:#222"><use href="#i-caret"/></svg></div>
  <svg class="bell" style="fill:#222"><use href="#i-bell"/></svg>
  <div class="user"><span class="user__avatar" role="img" aria-label="User avatar photo"></span>Sam Reed</div>

  <h1 class="budget-title">BUDGET</h1>

  <svg class="charts" viewBox="0 0 1408 922" font-family="Roboto, sans-serif">
    <!-- radial budget chart -->
    <g fill="none" stroke-width="8" stroke-linecap="round" transform="rotate(-90 419 323)">
      <circle cx="419" cy="323" r="135" stroke="#8bc34a" stroke-dasharray="661.6 1000"/>
      <circle cx="419" cy="323" r="117" stroke="#3b9be0" stroke-dasharray="639.5 1000"/>
      <circle cx="419" cy="323" r="99" stroke="#f5a742" stroke-dasharray="410.5 1000"/>
      <circle cx="419" cy="323" r="81" stroke="#ee3d52" stroke-dasharray="325.7 1000"/>
      <circle cx="419" cy="323" r="63" stroke="#a8161c" stroke-dasharray="221.7 1000"/>
    </g>
    <g fill="none" stroke="#bbb" stroke-width="1">
      <polyline points="555,290 583,290 583,187 641,187"/>
      <polyline points="555,305 598,305 598,256 641,256"/>
      <polyline points="560,323 641,323"/>
      <polyline points="555,340 597,340 597,393 641,393"/>
      <polyline points="555,355 581,355 581,461 641,461"/>
    </g>
    <g fill="#bbb">
      <circle cx="641" cy="187" r="2.5"/><circle cx="641" cy="256" r="2.5"/><circle cx="641" cy="323" r="2.5"/><circle cx="641" cy="393" r="2.5"/><circle cx="641" cy="461" r="2.5"/>
    </g>
    <g font-size="17" font-weight="500" dominant-baseline="middle">
      <text x="653" y="187" fill="#8bc34a">645715 21.4%</text>
      <text x="653" y="256" fill="#3b9be0">219000 28.6%</text>
      <text x="653" y="324" fill="#f5a742">426715 14.1%</text>
      <text x="653" y="393" fill="#ee3d52">390488 12.9%</text>
      <text x="653" y="461" fill="#a8161c">219000 7.25%</text>
    </g>

    <!-- left bar chart -->
    <text x="530" y="535" font-size="11" font-weight="500" text-anchor="middle" fill="#222">30/11/2019</text>
    <text transform="translate(259 705) rotate(-90)" font-size="11" font-weight="700" text-anchor="middle" fill="#222">Value</text>
    <g font-size="8" fill="#333" text-anchor="end" dominant-baseline="middle">
      <text x="298" y="573">1m</text><text x="298" y="606">0.8m</text><text x="298" y="640">0.6m</text><text x="298" y="673">0.4m</text><text x="298" y="707">0.2m</text><text x="298" y="740">0</text><text x="298" y="773">-0.2m</text><text x="298" y="807">-0.4m</text>
      <text x="892" y="573">1m</text><text x="892" y="606">0.8m</text><text x="892" y="640">0.6m</text><text x="892" y="673">0.4m</text><text x="892" y="707">0.2m</text><text x="892" y="740">0</text><text x="892" y="773">-0.2m</text><text x="892" y="807">-0.4m</text>
    </g>
    <g stroke="#555" stroke-width="1">
      <line x1="309" y1="558" x2="309" y2="808"/><line x1="309" y1="808" x2="756" y2="808"/><line x1="309" y1="740" x2="756" y2="740" stroke="#ccc"/>
      <line x1="903" y1="558" x2="903" y2="808"/><line x1="903" y1="808" x2="1349" y2="808"/><line x1="903" y1="740" x2="1349" y2="740" stroke="#ccc"/>
    </g>
    <g fill="#2b35a0">
      <rect x="327" y="653" width="12" height="87" rx="6"/>
      <rect x="349" y="692" width="12" height="48" rx="6"/>
      <rect x="370" y="736" width="12" height="6" rx="3"/>
      <rect x="388" y="736" width="12" height="6" rx="3"/>
      <rect x="409" y="740" width="12" height="50" rx="6"/>
      <rect x="430" y="606" width="12" height="134" rx="6"/>
      <rect x="452" y="653" width="12" height="87" rx="6"/>
      <rect x="474" y="675" width="12" height="65" rx="6"/>
      <rect x="494" y="736" width="12" height="6" rx="3"/>
      <rect x="512" y="736" width="12" height="6" rx="3"/>
      <rect x="534" y="727" width="12" height="13" rx="6"/>
      <rect x="556" y="733" width="12" height="7" rx="3.5"/>
      <rect x="576" y="736" width="12" height="6" rx="3"/>
      <rect x="593" y="736" width="12" height="6" rx="3"/>
      <rect x="617" y="736" width="12" height="6" rx="3"/>
      <rect x="634" y="736" width="12" height="6" rx="3"/>
      <rect x="659" y="736" width="12" height="6" rx="3"/>
      <rect x="677" y="736" width="12" height="6" rx="3"/>
      <rect x="701" y="636" width="12" height="104" rx="6"/>
      <rect x="724" y="653" width="12" height="87" rx="6"/>

      <rect x="921" y="653" width="12" height="87" rx="6"/>
      <rect x="943" y="723" width="12" height="17" rx="6"/>
      <rect x="966" y="736" width="12" height="6" rx="3"/>
      <rect x="1003" y="736" width="12" height="6" rx="3"/>
      <rect x="1024" y="606" width="12" height="134" rx="6"/>
      <rect x="1088" y="736" width="12" height="6" rx="3"/>
      <rect x="1106" y="736" width="12" height="6" rx="3"/>
      <rect x="1128" y="727" width="12" height="13" rx="6"/>
      <rect x="1150" y="733" width="12" height="7" rx="3.5"/>
      <rect x="1171" y="736" width="12" height="6" rx="3"/>
      <rect x="1188" y="736" width="12" height="6" rx="3"/>
      <rect x="1229" y="736" width="12" height="6" rx="3"/>
      <rect x="1253" y="736" width="12" height="6" rx="3"/>
      <rect x="1271" y="736" width="12" height="6" rx="3"/>
      <rect x="1295" y="636" width="12" height="104" rx="6"/>
      <rect x="1318" y="740" width="12" height="50" rx="6"/>
    </g>
    <g font-size="8" fill="#333">
      <text transform="translate(336 650) rotate(-90)">538715.38</text>
      <text transform="translate(358 689) rotate(-90)">538715.38</text>
      <text transform="translate(379 733) rotate(-90)">538715.38</text>
      <text transform="translate(397 733) rotate(-90)">538715.38</text>
      <text transform="translate(418 793) rotate(90)" text-anchor="start">538715.38</text>
      <text transform="translate(439 603) rotate(-90)">538715.38</text>
      <text transform="translate(461 650) rotate(-90)">538715.38</text>
      <text transform="translate(483 672) rotate(-90)">538715.38</text>
      <text transform="translate(503 733) rotate(-90)">538715.38</text>
      <text transform="translate(521 733) rotate(-90)">538715.38</text>
      <text transform="translate(543 724) rotate(-90)">538715.38</text>
      <text transform="translate(565 730) rotate(-90)">538715.38</text>
      <text transform="translate(585 733) rotate(-90)">538715.38</text>
      <text transform="translate(602 733) rotate(-90)">538715.38</text>
      <text transform="translate(626 733) rotate(-90)">538715.38</text>
      <text transform="translate(643 733) rotate(-90)">538715.38</text>
      <text transform="translate(668 733) rotate(-90)">538715.38</text>
      <text transform="translate(686 733) rotate(-90)">538715.38</text>
      <text transform="translate(710 633) rotate(-90)">538715.38</text>
      <text transform="translate(733 650) rotate(-90)">538715.38</text>

      <text transform="translate(930 650) rotate(-90)">538715.38</text>
      <text transform="translate(952 720) rotate(-90)">538715.38</text>
      <text transform="translate(975 733) rotate(-90)">538715.38</text>
      <text transform="translate(991 737) rotate(-90)">538715.38</text>
      <text transform="translate(1012 733) rotate(-90)">538715.38</text>
      <text transform="translate(1033 603) rotate(-90)">538715.38</text>
      <text transform="translate(1055 737) rotate(-90)">538715.38</text>
      <text transform="translate(1077 737) rotate(-90)">538715.38</text>
      <text transform="translate(1097 733) rotate(-90)">538715.38</text>
      <text transform="translate(1115 733) rotate(-90)">538715.38</text>
      <text transform="translate(1137 724) rotate(-90)">538715.38</text>
      <text transform="translate(1159 730) rotate(-90)">538715.38</text>
      <text transform="translate(1180 733) rotate(-90)">538715.38</text>
      <text transform="translate(1197 733) rotate(-90)">538715.38</text>
      <text transform="translate(1219 737) rotate(-90)">538715.38</text>
      <text transform="translate(1238 733) rotate(-90)">538715.38</text>
      <text transform="translate(1262 733) rotate(-90)">538715.38</text>
      <text transform="translate(1280 733) rotate(-90)">538715.38</text>
      <text transform="translate(1304 633) rotate(-90)">538715.38</text>
      <text transform="translate(1327 793) rotate(90)">538715.38</text>
    </g>
    <g font-size="8" fill="#333">
      <text transform="translate(306 820) rotate(90)">Revenue</text>
      <text transform="translate(327 820) rotate(90)">Supplies and equipment</text>
      <text transform="translate(348 820) rotate(90)">Community awareness</text>
      <text transform="translate(369 820) rotate(90)">Depreciation</text>
      <text transform="translate(390 820) rotate(90)">Business insurance</text>
      <text transform="translate(411 820) rotate(90)">Travel</text>
      <text transform="translate(432 820) rotate(90)">Information</text>
      <text transform="translate(453 820) rotate(90)">Friends</text>
      <text transform="translate(474 820) rotate(90)">Online donation</text>
      <text transform="translate(495 820) rotate(90)">Special events</text>
      <text transform="translate(516 820) rotate(90)">Professional</text>
      <text transform="translate(537 820) rotate(90)">Youth activities</text>
      <text transform="translate(558 820) rotate(90)">Payroll</text>
      <text transform="translate(579 820) rotate(90)">individual</text>
      <text transform="translate(600 820) rotate(90)">Benefits</text>
      <text transform="translate(621 820) rotate(90)">Rent</text>
      <text transform="translate(642 820) rotate(90)">Foundation contributions</text>
      <text transform="translate(663 820) rotate(90)">Total revenue</text>
      <text transform="translate(684 820) rotate(90)">Salaries and wages</text>
      <text transform="translate(705 820) rotate(90)">Net Surplus (Deficit)</text>
      <text transform="translate(726 820) rotate(90)">Total Expenses</text>
      <text transform="translate(747 820) rotate(90)">Net Surplus</text>

      <text transform="translate(900 820) rotate(90)">Revenue</text>
      <text transform="translate(921 820) rotate(90)">Supplies and equipment</text>
      <text transform="translate(942 820) rotate(90)">Community awareness</text>
      <text transform="translate(963 820) rotate(90)">Depreciation</text>
      <text transform="translate(984 820) rotate(90)">Business insurance</text>
      <text transform="translate(1005 820) rotate(90)">Travel</text>
      <text transform="translate(1026 820) rotate(90)">Information</text>
      <text transform="translate(1047 820) rotate(90)">Friends</text>
      <text transform="translate(1068 820) rotate(90)">Online donation</text>
      <text transform="translate(1089 820) rotate(90)">Special events</text>
      <text transform="translate(1110 820) rotate(90)">Professional</text>
      <text transform="translate(1131 820) rotate(90)">Youth activities</text>
      <text transform="translate(1152 820) rotate(90)">Payroll</text>
      <text transform="translate(1173 820) rotate(90)">individual</text>
      <text transform="translate(1194 820) rotate(90)">Benefits</text>
      <text transform="translate(1215 820) rotate(90)">Rent</text>
      <text transform="translate(1236 820) rotate(90)">Foundation contributions</text>
      <text transform="translate(1257 820) rotate(90)">Total revenue</text>
      <text transform="translate(1278 820) rotate(90)">Salaries and wages</text>
      <text transform="translate(1299 820) rotate(90)">Net Surplus (Deficit)</text>
      <text transform="translate(1320 820) rotate(90)">Total Expenses</text>
      <text transform="translate(1341 820) rotate(90)">Net Surplus</text>
    </g>

    <!-- right bar chart -->
    <text x="1117" y="535" font-size="11" font-weight="500" text-anchor="middle" fill="#222">Variance</text>
    <text transform="translate(853 705) rotate(-90)" font-size="11" font-weight="700" text-anchor="middle" fill="#222">Value</text>
  </svg>

  <ul class="legend">
    <li><i style="background:#5b6ee8"></i>TOTAL</li>
    <li><i style="background:#ee4b3a"></i>TOTAL EXPENSES</li>
    <li><i style="background:#1bb08a"></i>NET SURPLUS (DEFICIT)</li>
    <li><i style="background:#a35be6"></i>SALARIES AND WAGES</li>
    <li><i style="background:#f59a4a"></i>TOTAL REVENUE</li>
    <li><i style="background:#22c1e0"></i>FOUNDATION CONTRIBUTIONS</li>
    <li><i style="background:#f5557a"></i>RENT</li>
    <li><i style="background:#a5d872"></i>BENEFITS</li>
    <li><i style="background:#f07ef0"></i>INDIVIDUAL</li>
    <li><i style="background:#f6c548"></i>PAYROLL</li>
    <li><i style="background:#c3c8f0"></i>YOUTH ACTIVITIES</li>
    <li><i style="background:#f0a090"></i>PROFESSIONAL</li>
    <li><i style="background:#4ee8b0"></i>SPECIAL EVENTS</li>
    <li><i style="background:#d9c3f2"></i>ONLINE DONATION</li>
    <li><i style="background:#fbd9bd"></i>FRIENDS</li>
    <li><i style="background:#8fdcf0"></i>INFORMATION</li>
    <li><i style="background:#f9c6d6"></i>TRAVEL</li>
  </ul>
</section>

</body>
</html>
```